Label Design for a New Alcoholized Root Beer

Create a design for a new alcoholized root beer. This is a new product category in the USA growing very rapidly. Root Beer is a popular flavor of Cola, but recently, beer manufacturers have added alcohol to it and have created a new product that has gained traction on the market at a tremendous rate.

Root Beer is vintage product that has been around for a hundred years. Consumers of this product are mostly male between the age of 30 to 45. They purchase this product for its nostalgia and vintage look and taste.

This product will be in a standard 355 mL brown bottle.

It is 5.9% abv.

The name of the product is ''Corvel's Hard Root Beer''.

We have uploaded some pictures of traditional root beers to give you an idea of the feel we want our product to have and also, the bottle the product will be filled in.

Target Market(s)

Consumers are male 30-45, same market as craft beer consumers

Industry/Entity Type

Product

Requirements
Must have
• Design must have a vintage feel to it

```html
<!DOCTYPE html>
<html lang="en">
<head>
<meta charset="utf-8">
<title>Corvel's Hard Root Beer – Label</title>
<link rel="stylesheet" href="https://fonts.googleapis.com/css2?family=Rye&family=Open+Sans:wght@400&display=swap">
<style>
  :root {
    --paper: #ffffff;
    --amber: #e09a1e;
    --brick: #b83a2a;
    --olive: #6f6a3b;
    --leaf: #4e6a2e;
    --cream: #fbe8a4;
    --ink: #2f2a1c;
  }
  html, body {
    margin: 0;
    padding: 0;
    width: 1200px;
    height: 1000px;
    overflow: hidden;
    background: var(--paper);
  }
  .canvas {
    position: relative;
    width: 1200px;
    height: 1000px;
  }
  .label {
    position: absolute;
    left: 202px;
    top: 156px;
    width: 796px;
    height: 688px;
  }
  .band-edge { fill: var(--amber); }
  .band-red { fill: var(--brick); }
  .band-olive { fill: var(--olive); }
  .leaf-ring { fill: var(--amber); }
  .leaf-art { fill: var(--leaf); }
  .brand-name {
    font-family: "Rye", serif;
    fill: var(--cream);
  }
  .product-line {
    font-family: "Rye", serif;
    fill: var(--cream);
  }
  .abv {
    font-family: "Open Sans", sans-serif;
    fill: var(--ink);
  }
</style>
</head>
<body>
<main class="canvas">
  <svg class="label" viewBox="0 0 442 382" xmlns="http://www.w3.org/2000/svg">
    <g class="leaf-emblem">
      <circle class="leaf-ring" cx="117" cy="92" r="86"/>
      <circle class="leaf-art" cx="117" cy="92" r="78" role="img" aria-label="Illustration of a green root leaf"/>
    </g>
    <polygon class="band-edge" points="0,190 442,94 442,382 0,382"/>
    <polygon class="band-red" points="0,198 442,102 442,229 0,326"/>
    <polygon class="band-olive" points="0,336 442,238 442,382 0,382"/>
    <text class="brand-name" x="36" y="292" font-size="78" textLength="376" lengthAdjust="spacingAndGlyphs">CORVEL'S</text>
    <text class="product-line" x="132" y="346" font-size="27" textLength="290" lengthAdjust="spacingAndGlyphs">HARD ROOT BEER</text>
    <text class="abv" x="318" y="372" font-size="17">5.9% ABV.</text>
  </svg>
</main>
</body>
</html>
```